Book Cover Design Project

A non-fiction book on child protection, specifically... keeping young children safe from predators and keeping teenagers safe from themselves.

Title:
Under Our Roof

Subtitle:
A Guide To Keeping Your Children Safe

Author:
Martin Kellerby

```html
<!DOCTYPE html>
<html lang="en">
<head>
<meta charset="utf-8">
<title>Under Our Roof — Martin Kellerby</title>
<link rel="stylesheet" href="https://fonts.googleapis.com/css2?family=Open+Sans:wght@400;700&display=swap">
<style>
  :root {
    --cover-yellow: #fff200;
    --figure-cyan: #00aeef;
    --figure-navy: #2b2a6b;
    --title-red: #c4161c;
    --title-yellow: #fff200;
    --band-black: #231f20;
    --band-text: #ffffff;
    --author-ink: #231f20;
  }
  * { margin: 0; padding: 0; box-sizing: border-box; }
  html, body {
    width: 756px;
    height: 1200px;
    overflow: hidden;
    background: var(--cover-yellow);
  }
  .cover {
    position: relative;
    width: 756px;
    height: 1200px;
    background: var(--cover-yellow);
    font-family: "Open Sans", Arial, sans-serif;
  }
  .cover-figure {
    position: absolute;
    left: 0;
    top: 0;
    width: 756px;
    height: 892px;
  }
  .book-title {
    position: absolute;
    left: 75px;
    top: 582px;
    font-size: 50px;
    font-weight: 700;
    line-height: 1;
    letter-spacing: -0.5px;
    text-transform: lowercase;
    white-space: nowrap;
  }
  .book-title .title-lead { color: var(--title-red); }
  .book-title .title-accent { color: var(--title-yellow); }
  .subtitle-band {
    position: absolute;
    left: 0;
    top: 892px;
    width: 756px;
    height: 133px;
    background: var(--band-black);
    display: flex;
    align-items: center;
    justify-content: center;
  }
  .subtitle {
    color: var(--band-text);
    font-size: 33px;
    font-weight: 400;
    letter-spacing: 0.2px;
  }
  .author {
    position: absolute;
    left: 0;
    top: 1062px;
    width: 756px;
    text-align: center;
    color: var(--author-ink);
    font-size: 23px;
    font-weight: 400;
  }
</style>
</head>
<body>
  <main class="cover">
    <svg class="cover-figure" viewBox="0 0 756 892" role="img" aria-label="Silhouette illustration of a mother cradling a newborn baby against her chest">
      <defs>
        <linearGradient id="figure-tone" x1="0" y1="0" x2="1" y2="0">
          <stop offset="0" stop-color="var(--figure-navy)"/>
          <stop offset="0.35" stop-color="var(--figure-cyan)"/>
          <stop offset="1" stop-color="var(--figure-cyan)"/>
        </linearGradient>
      </defs>
      <path d="M330 892 L330 330 Q330 120 480 120 Q640 120 690 330 L712 892 Z" fill="url(#figure-tone)"/>
    </svg>

    <h1 class="book-title"><span class="title-lead">Under Our </span><span class="title-accent">Roof</span></h1>

    <div class="subtitle-band">
      <p class="subtitle">A Guide To Keeping Your Children Safe</p>
    </div>

    <p class="author">Martin Kellerby</p>
  </main>
</body>
</html>
```